Company letter head and business card for new Indian Pharmaceutical Export company.

We need a letterhead and business card design for an Indian Pharmaceutical Export company.

The letter head needs to contain the following information.
Vorin Healthline Pvt. Ltd.
Office No 4827 Plot No 19, Larkspire, KT Lane, 400153, Maharashtra, India.
Email: info@vorin-healthline.com
Phone: +91-8342196507
CIN: U71853MH2025PTC902617
GSTIN: (This number is still pending, we will add later)

The business card needs to contain:
Address:
Vorin Healthline Pvt. Ltd.
Office No 4827 Plot No19, Larkspire, KT Lane, 400153, MH, India.
Email: torvald@vorin-healthline.com
Phone: +49-17634902851
Name on card: Torvald Ramming
Position: Director

The design for the letter head and business card should be simple but trustworthy.
Please use only Green and blue, same as in the attached logo.

```html
<!DOCTYPE html>
<html lang="en">
<head>
<meta charset="utf-8">
<title>Vorin Healthline – Letterhead and Business Card</title>
<link href="https://fonts.googleapis.com/css2?family=Open+Sans:wght@400&family=Poppins:wght@300;400;500;600;700&display=swap" rel="stylesheet">
<style>
  :root{
    --blue:#0a5ea2;
    --green:#8bc43f;
    --ink:#3d3d3d;
    --body:#9a9a9a;
    --paper:#ffffff;
    --backdrop:#dddfe1;
    --shadow:0 4px 10px rgba(0,0,0,.18);
  }
  *{box-sizing:border-box;margin:0;padding:0}
  html,body{width:1200px;height:913px;overflow:hidden;background:var(--backdrop)}
  body{position:relative;font-family:"Open Sans",sans-serif;color:var(--ink)}
  .icon-defs{position:absolute;width:0;height:0}

  /* shared */
  .brand{position:absolute;text-align:center}
  .brand__mark{display:block;margin:0 auto;border-radius:50%;background:var(--blue)}
  .brand__name{display:block;font-family:"Poppins",sans-serif;font-weight:700;color:var(--blue);white-space:nowrap}
  .ico{display:inline-block;flex:none;width:11px;height:11px;border-radius:1.5px;vertical-align:middle;position:relative}
  .ico svg{position:absolute;inset:1.5px;width:8px;height:8px;fill:#fff}
  .ico--blue{background:var(--blue)}
  .ico--green{background:var(--green)}
  .band{position:absolute;height:8px;display:flex}
  .band__green{background:var(--green);clip-path:polygon(0 0,100% 0,calc(100% - 6px) 100%,0 100%)}
  .band__blue{flex:1;background:var(--blue);margin-left:-3px;clip-path:polygon(6px 0,100% 0,100% 100%,0 100%)}

  /* letterhead */
  .letterhead{position:absolute;left:99px;top:76px;width:542px;height:761px;background:var(--paper);box-shadow:var(--shadow)}
  .letterhead .brand{left:40px;top:36px;width:106px}
  .letterhead .brand__mark{width:80px;height:80px}
  .letterhead .brand__name{font-size:11px;margin-top:9px}
  .sender{position:absolute;left:48px;top:182px}
  .sender__name{font-family:"Poppins",sans-serif;font-weight:600;font-size:15px;color:var(--blue);line-height:1.2}
  .sender__role{font-size:8.5px;font-weight:400;color:var(--ink);margin-top:1px}
  .sender__list{list-style:none;margin-top:8px;font-size:10px;line-height:15.2px}
  .sender__list b{display:inline-block;width:19px;color:var(--green);font-weight:400}
  .letter-date{position:absolute;right:49px;top:266px;font-size:12px;color:var(--ink)}
  .letter-body{position:absolute;left:48px;top:307px;width:445px;font-size:9.6px;line-height:14.15px;color:var(--body);text-align:justify}
  .letter-body p+p{margin-top:14px}
  .signature{position:absolute;right:59px;top:541px;width:79px;height:49px;background:linear-gradient(135deg,#f1f1f1,#e6e6e6);border-radius:3px}
  .signer{position:absolute;right:49px;top:596px;font-family:"Poppins",sans-serif;font-size:12.5px;color:var(--ink)}
  .lh-contacts{position:absolute;left:51px;top:618px;list-style:none;font-family:"Poppins",sans-serif;font-weight:300;font-size:8.6px;color:var(--ink)}
  .lh-contacts li{display:flex;align-items:flex-start;gap:3px;line-height:10px;margin-bottom:6px}
  .lh-contacts li:first-child{margin-bottom:8px}
  .lh-contacts strong{font-weight:500;color:var(--blue)}
  .letterhead .band{left:0;right:0;top:731px}
  .letterhead .band__green{width:276px}

  /* business card front */
  .card{position:absolute;left:697px;width:379px;height:227px;background:var(--paper);box-shadow:var(--shadow)}
  .card--front{top:135px}
  .card--front .brand{left:30px;top:43px;width:110px}
  .card--front .brand__mark{width:100px;height:100px}
  .card--front .brand__name{font-size:13.5px;margin-top:6px}
  .holder{position:absolute;right:27px;top:26px;text-align:right;font-family:"Poppins",sans-serif}
  .holder__name{font-size:13.5px;font-weight:700;letter-spacing:.2px;line-height:1.1}
  .holder__first{color:var(--green)}
  .holder__last{color:var(--blue)}
  .holder__role{font-size:8.6px;font-weight:300;line-height:11px;color:var(--ink);margin-top:1px;padding-bottom:3px;border-bottom:1px solid var(--ink);display:inline-block}
  .card-contacts{position:absolute;right:27px;top:106px;list-style:none;text-align:right;font-family:"Poppins",sans-serif;font-weight:300;font-size:8.8px;color:var(--ink)}
  .card-contacts li{display:flex;justify-content:flex-end;align-items:flex-start;gap:3px;line-height:10.5px;margin-bottom:7px}
  .card-contacts li:first-child{margin-bottom:9px}
  .card--front .band{left:23px;width:332px;top:192px}
  .card--front .band__green{width:172px}

  /* business card back */
  .card--back{top:412px}
  .card__tab{position:absolute;top:64px;width:19px;height:99px;background:var(--blue)}
  .card__tab--left{left:0;border-radius:0 6px 6px 0}
  .card__tab--right{right:0;border-radius:6px 0 0 6px}
  .card--back .brand{left:0;right:0;top:46px}
  .card--back .brand__mark{width:112px;height:112px}
  .card--back .brand__name{font-size:15px;margin-top:9px}
</style>
</head>
<body>

<svg class="icon-defs" aria-hidden="true">
  <symbol id="i-pin" viewBox="0 0 10 10"><path d="M5 0.5a3.3 3.3 0 0 0-3.3 3.3C1.7 6.3 5 9.5 5 9.5s3.3-3.2 3.3-5.7A3.3 3.3 0 0 0 5 .5zm0 4.6a1.3 1.3 0 1 1 0-2.6 1.3 1.3 0 0 1 0 2.6z"/></symbol>
  <symbol id="i-phone" viewBox="0 0 10 10"><path d="M2.3 .8l1.6 1.9-.9 1.1c.6 1.2 1.5 2.1 2.7 2.7l1.1-.9 1.9 1.6-1 1.6C4.5 8.5 1.5 5.5 .7 2.3z"/></symbol>
  <symbol id="i-mail" viewBox="0 0 10 10"><path d="M.5 2h9v6h-9zM1.3 2.6L5 5.6l3.7-3H1.3zM1.2 3.3v4.1h7.6V3.3L5 6.4z" fill-rule="evenodd"/></symbol>
  <symbol id="i-pointer" viewBox="0 0 10 10"><path d="M2.5 .5l5.5 5.2-2.6.2 1.5 3.2-1.1.5-1.5-3.2L2.5 8.3z"/></symbol>
  <symbol id="i-doc" viewBox="0 0 10 10"><path d="M2 .5h4.2L8 2.3v7.2H2zM3 4h4v.9H3zM3 5.7h4v.9H3zM3 7.4h2.8v.9H3z" fill-rule="evenodd"/></symbol>
</svg>

<!-- Letterhead -->
<section class="letterhead" aria-label="Letterhead">
  <div class="brand">
    <span class="brand__mark"></span>
    <span class="brand__name">Vorin Healthline</span>
  </div>

  <div class="sender">
    <h1 class="sender__name">Elian Varsk</h1>
    <p class="sender__role">Chief Director</p>
    <ul class="sender__list">
      <li><b>A :</b>7312 Hollin Ridge, Castmere 40718</li>
      <li><b>W :</b>www.vorin-healthline.com</li>
      <li><b>P :</b>+91 834 219 65</li>
      <li><b>M :</b>office@vorin-healthline.com</li>
    </ul>
  </div>

  <p class="letter-date">12 December, 2025</p>

  <div class="letter-body">
    <p>Lorem ipsum dolor sit amet, consectetuer adipiscing elit, sed diam nonummy nibh euismod tincidunt ut laoreet dolore magna aliquam erat volutpat. Ut wisi enim ad minim veniam, quis nostrud exerci tation ullamcorper suscipit lobortis nisl ut aliquip ex ea commodo consequat. Duis autem vel eum iriure dolor in hendrerit in vulputate velit esse molestie consequat, vel illum dolore eu feugiat nulla facilisis at vero eros et accumsan et iusto odio dignissim qui blandit praesent luptatum zzril delenit augue duis dolore te feugait nulla facilisi.</p>
    <p>Lorem ipsum dolor sit amet, cons ectetuer adipiscing elit, sed diam nonummy nibh euismod tincidunt ut laoreet dolore magna aliquam erat volutpat. Ut wisi enim ad minim veniam, quis nostrud exerci tation ullamcorper suscipit lobortis nisl ut aliquip ex ea commodo consequat.</p>
    <p>Lorem ipsum dolor sit amet, consectetuer adipiscing elit, sed diam nonummy nibh euismod tincidunt ut laoreet dolore magna aliquam eratveniam, quis nostrud exerci tation ullamcorper suscipit lobortis nisl ut aliquip ex ea commodo consequat. Lorem ipsum dolor sit zamet, consectetuer adipiscing elit, sed diam nonummy nibh euismod tincidunt.</p>
  </div>

  <div class="signature" role="img" aria-label="Handwritten signature"></div>
  <p class="signer">Mr. Elian Varsk</p>

  <ul class="lh-contacts">
    <li><span class="ico ico--green"><svg><use href="#i-pin"/></svg></span><span><strong>Vorin Healthline Pvt. Ltd.</strong><br>Office No 4827 Plot No 19, Larkspire, KT Lane,<br>400153, Maharashtra, India.</span></li>
    <li><span class="ico ico--blue"><svg><use href="#i-phone"/></svg></span><span>+91-8342196507</span></li>
    <li><span class="ico ico--blue"><svg><use href="#i-mail"/></svg></span><span>info@vorin-healthline.com</span></li>
    <li><span class="ico ico--blue"><svg><use href="#i-pointer"/></svg></span><span>vorin-healthline.com</span></li>
    <li><span class="ico ico--blue"><svg><use href="#i-doc"/></svg></span><span>CIN: U71853MH2025PTC902617</span></li>
  </ul>

  <div class="band"><span class="band__green"></span><span class="band__blue"></span></div>
</section>

<!-- Business card, front -->
<section class="card card--front" aria-label="Business card front">
  <div class="brand">
    <span class="brand__mark"></span>
    <span class="brand__name">Vorin Healthline</span>
  </div>

  <div class="holder">
    <h2 class="holder__name"><span class="holder__first">TORVALD</span> <span class="holder__last">RAMMING</span></h2>
    <p class="holder__role">Director</p>
  </div>

  <ul class="card-contacts">
    <li><span>4827 Plot No19, Larkspire<br>KT Lane, 400153, MH, India.</span><span class="ico ico--blue"><svg><use href="#i-pin"/></svg></span></li>
    <li><span>+49-17634902851</span><span class="ico ico--green"><svg><use href="#i-phone"/></svg></span></li>
    <li><span>torvald@vorin-healthline.com</span><span class="ico ico--green"><svg><use href="#i-mail"/></svg></span></li>
    <li><span>vorin-healthline.com</span><span class="ico ico--green"><svg><use href="#i-pointer"/></svg></span></li>
  </ul>

  <div class="band"><span class="band__green"></span><span class="band__blue"></span></div>
</section>

<!-- Business card, back -->
<section class="card card--back" aria-label="Business card back">
  <span class="card__tab card__tab--left"></span>
  <span class="card__tab card__tab--right"></span>
  <div class="brand">
    <span class="brand__mark"></span>
    <span class="brand__name">Vorin Healthline</span>
  </div>
</section>

</body>
</html>
```